Business card design needed

We are a wine business involved in winemaking, broking and packaging on behalf of clients globally with the majority being Asian. The design should be quite traditional and classic with some red used, font used should be easily read.

Target Market(s)

Trade customers other business owners

Industry/Entity Type

Business

Contact Information for Business Card

Rosalind Thwaite
Meridale Wine Collective
PO Box 738, Fenwick Vale
South Australia 5187
Phone: +61 (0)455 982 317
Email: kvcellars@brightmail.example

Logo styles of interest
Lettermark Logo

```html
<!DOCTYPE html>
<html lang="en">
<head>
<meta charset="utf-8">
<title>Meridale Wine Collective – Business Card</title>
<link rel="stylesheet" href="https://fonts.googleapis.com/css2?family=Cinzel:wght@400;700&display=swap">
<style>
  :root {
    --page: #ffffff;
    --card-edge: #000000;
    --card-glow: #d42222;
    --card-mid: #6e0b0b;
    --rule-red: #e0292b;
    --ink-light: #f2eeee;
    --ink-dark: #1a1414;
  }
  html, body {
    margin: 0;
    padding: 0;
    width: 1071px;
    height: 1200px;
    overflow: hidden;
    background: var(--page);
  }
  .canvas {
    position: relative;
    width: 1071px;
    height: 1200px;
  }
  .business-card {
    position: absolute;
    left: 208px;
    top: 434px;
    width: 688px;
    height: 392px;
    background: radial-gradient(ellipse 46% 52% at 50% 50%, var(--card-glow) 0%, var(--card-mid) 55%, var(--card-edge) 100%);
    color: var(--ink-light);
    font-family: "Cinzel", serif;
    overflow: hidden;
  }
  .frame-rule {
    position: absolute;
  }
  .frame-rule--top,
  .frame-rule--bottom {
    left: 24px;
    right: 24px;
    height: 3px;
    background: linear-gradient(90deg, transparent 0%, var(--rule-red) 50%, transparent 100%);
  }
  .frame-rule--top { top: 18px; }
  .frame-rule--bottom { bottom: 18px; }
  .frame-rule--left,
  .frame-rule--right {
    top: 34px;
    bottom: 34px;
    width: 3px;
    background: linear-gradient(180deg, transparent 0%, var(--rule-red) 50%, transparent 100%);
  }
  .frame-rule--left { left: 22px; }
  .frame-rule--right { right: 22px; }
  .contact-lines {
    position: absolute;
    top: 36px;
    left: 0;
    right: 0;
    text-align: center;
    font-size: 14px;
    letter-spacing: 1.6px;
    line-height: 18px;
    font-variant: small-caps;
  }
  .contact-lines p { margin: 0; }
  .wordmark {
    position: absolute;
    top: 150px;
    left: 0;
    right: 0;
    text-align: center;
    font-weight: 700;
    font-size: 40px;
    line-height: 48px;
    color: var(--ink-dark);
    letter-spacing: 1px;
  }
  .postal-address {
    position: absolute;
    top: 318px;
    left: 0;
    right: 0;
    text-align: center;
    font-size: 14px;
    letter-spacing: 1.6px;
    line-height: 18px;
    font-variant: small-caps;
  }
  .postal-address p { margin: 0; }
</style>
</head>
<body>
<div class="canvas">
  <section class="business-card">
    <span class="frame-rule frame-rule--top"></span>
    <span class="frame-rule frame-rule--bottom"></span>
    <span class="frame-rule frame-rule--left"></span>
    <span class="frame-rule frame-rule--right"></span>

    <div class="contact-lines">
      <p>Phone: +61 (0)455 982 317</p>
      <p>Email: kvcellars@brightmail.example</p>
    </div>

    <div class="wordmark">Meridale<br>Wine Collective</div>

    <address class="postal-address">
      <p>Rosalind Thwaite Meridale Wine Collective, PO Box 738,</p>
      <p>Fenwick Vale South Australia 5187</p>
    </address>
  </section>
</div>
</body>
</html>
```